Business Card Design

I require the design of business cards using my exisiting logo.

It is essential that the designer has experience with various print processes (foil stamping etc) and different paper stock.

The design is to blend in with current packaging and display unit. (Images will be provided).
A swing tag and certificate of authenticity design will als be required at a later stage.

Details which need to be included on the card are:
- Contact Name
- Position in Company
- Address
- Contact Number
- Email Address
- Web Address

Ideally I would prefer the background (both sides) to be greyish colour (offset printing or if you can suggest greyish paperstock) with silver foiling on the front and either black or metallic silver on the back.

Or another option would be grey background on the front and either white or black on the the back.

* The business card can be portrait or landscape.

Printers specifications:
Bleed 3mm
Trim Marks
Seperate file for foil printing

This task is for someone who is creative and enjoys working with fashion and luxury items!
_______________________________________________

I will require business cards designs for 2 different business and would hope to work with the same designer.

Please note I had asked for a grey colour at least on one of the sides. However I keep on getting black and white designs.   

Business

• - Double sided business card
- Luxury feel
- Foil Print Priniting

- Would prefer at least grey background at least on one side of the card.

- The business card can be portrait or landscape.
• *The business card can be portrait or landscape.
• - Bright Colours
- Alterations to logo

```html
<!DOCTYPE html>
<html lang="en">
<head>
<meta charset="UTF-8">
<title>Orin Jewels – Business Card</title>
<link href="https://fonts.googleapis.com/css2?family=Open+Sans:wght@300;400;700&display=swap" rel="stylesheet">
<style>
  :root {
    --page-bg: #ecebe8;
    --card-grey: #c8c9cb;
    --ink-dark: #1c1c1c;
    --ink-mid: #55575a;
    --ink-soft: #6a6c6f;
  }
  * { margin: 0; padding: 0; box-sizing: border-box; }
  html, body {
    width: 1200px; height: 758px; overflow: hidden;
    background: var(--page-bg);
    font-family: "Open Sans", sans-serif;
  }
  .stage { position: relative; width: 1200px; height: 758px; }
  .card {
    position: absolute;
    width: 520px; height: 300px;
    background: var(--card-grey);
    border-radius: 26px;
  }
  .card--front { left: 60px; top: 120px; }
  .card--back { left: 620px; top: 340px; }

  .brand {
    position: absolute; left: 100px; top: 62px;
    display: flex; align-items: center; gap: 18px;
  }
  .brand__dot {
    width: 62px; height: 62px; border-radius: 50%;
    border: 1.5px solid var(--ink-dark);
  }
  .brand__name {
    font-weight: 300; font-size: 44px; letter-spacing: 1px;
    color: var(--ink-dark); line-height: 1;
  }
  .address {
    position: absolute; left: 100px; top: 160px;
    font-size: 15px; color: var(--ink-mid); letter-spacing: .3px;
  }
  .contact {
    position: absolute; left: 180px; top: 200px;
    display: flex; gap: 10px; align-items: flex-start;
  }
  .person { text-align: right; padding-top: 18px; }
  .person__name { font-weight: 700; font-size: 15px; color: var(--ink-mid); }
  .person__role { font-size: 12px; color: var(--ink-soft); }
  .divider { width: 1px; height: 62px; background: var(--ink-soft); }
  .details { list-style: none; font-size: 12px; color: var(--ink-mid); line-height: 19px; }
  .details li { display: flex; align-items: center; gap: 5px; }
  .details svg { width: 9px; height: 9px; fill: var(--ink-mid); }

  .back-brand {
    position: absolute; left: 0; right: 0; top: 90px;
    display: flex; justify-content: center; align-items: center; gap: 16px;
  }
  .back-brand .brand__dot { width: 54px; height: 54px; }
  .back-brand .brand__name { font-size: 38px; }
  .back-web {
    position: absolute; left: 0; right: 0; top: 200px;
    text-align: center; font-size: 22px; letter-spacing: 3px;
    color: var(--ink-dark);
  }
</style>
</head>
<body>
<main class="stage">
  <section class="card card--front" aria-label="Business card front">
    <div class="brand">
      <span class="brand__dot"></span>
      <span class="brand__name">ORIN JEWELS</span>
    </div>
    <p class="address">00, Complex name, Street, City, Country, 000</p>
    <div class="contact">
      <div class="person">
        <p class="person__name">Your Name</p>
        <p class="person__role">Position</p>
      </div>
      <span class="divider"></span>
      <ul class="details">
        <li><svg viewBox="0 0 10 10"><path d="M2 0h2l1 3-1.5 1a6 6 0 0 0 2.5 2.5L7 5l3 1v2a2 2 0 0 1-2 2A8 8 0 0 1 0 2a2 2 0 0 1 2-2z"/></svg>+2340000000000</li>
        <li><svg viewBox="0 0 10 10"><rect x="0" y="2" width="10" height="7"/></svg>info@orinjewels.com</li>
        <li><svg viewBox="0 0 10 10"><circle cx="5" cy="5" r="4.5"/></svg>www.orinjewels.com</li>
      </ul>
    </div>
  </section>

  <section class="card card--back" aria-label="Business card back">
    <div class="back-brand">
      <span class="brand__dot"></span>
      <span class="brand__name">ORIN JEWELS</span>
    </div>
    <p class="back-web">www.orinjewels.com</p>
  </section>
</main>
</body>
</html>
```